Recycling Depot Business Card Design

We need a double sided business card for our recycling depot business. Please include name, position, address, phone, cell, fax, email and website address. Business card should match the colour scheme of our logo and look environmental but modern. I've attached a few business cards from Mintvale Works that I like.

Industry/Entity Type

Recycling

Contact Information for Business Card

Please include name, position, address, phone, cell, fax, email and website address.

Font styles to use
Sans Serif

Requirements
Must have
• Our Logo, Colour Scheme that matches our logo. Use of Colour Gradients and a custom look.

```html
<!DOCTYPE html>
<html lang="en">
<head>
<meta charset="utf-8">
<title>Greenloop Recovery – Business Card</title>
<link rel="stylesheet" href="https://fonts.googleapis.com/css2?family=Montserrat:wght@700&family=Questrial&display=swap">
<style>
  :root {
    --forest: #1f6637;
    --forest-light: #2a8c4d;
    --lime: #a6d13c;
    --lime-deep: #6cb543;
    --paper: #ffffff;
    --backdrop: #d4d4d4;
    --ink-green: #237a3f;
  }
  * { margin: 0; padding: 0; box-sizing: border-box; }
  html, body { width: 1200px; height: 800px; overflow: hidden; }
  body {
    background: var(--backdrop);
    position: relative;
    font-family: "Questrial", sans-serif;
  }
  .card {
    position: absolute;
    top: 245px;
    width: 540px;
    height: 309px;
    overflow: hidden;
    box-shadow: 0 6px 18px rgba(0,0,0,0.18);
  }
  .card--front {
    left: 40px;
    background: radial-gradient(ellipse at 42% 40%, var(--forest-light) 0%, var(--forest) 62%);
  }
  .card--back { left: 620px; background: var(--paper); }
  .card__shapes { position: absolute; inset: 0; }

  .brand {
    position: absolute;
    display: flex;
    align-items: center;
    gap: 12px;
    font-family: "Montserrat", sans-serif;
    font-weight: 700;
  }
  .brand__dot { border-radius: 50%; background: var(--lime); flex: none; }
  .card--front .brand {
    left: 50%; top: 50%;
    transform: translate(-50%, -50%);
    color: var(--paper);
    font-size: 40px;
    letter-spacing: -0.5px;
    white-space: nowrap;
  }
  .card--front .brand__dot { width: 38px; height: 38px; }
  .card--back .brand {
    left: 190px; top: 128px;
    color: var(--forest);
    font-size: 26px;
    white-space: nowrap;
  }
  .card--back .brand__dot { width: 26px; height: 26px; background: var(--lime-deep); }

  .holder {
    position: absolute;
    left: 24px; top: 26px;
    color: var(--paper);
  }
  .holder__name { font-family: "Montserrat", sans-serif; font-weight: 700; font-size: 21px; }
  .holder__role { font-size: 15px; margin-top: 2px; }

  .address {
    position: absolute;
    right: 26px; top: 190px;
    text-align: right;
    color: var(--ink-green);
    font-size: 14px;
    line-height: 1.35;
  }
  .contacts {
    position: absolute;
    left: 26px; bottom: 26px;
    list-style: none;
    color: var(--ink-green);
    font-size: 14px;
    line-height: 1.55;
  }
  .contacts li { display: flex; align-items: center; gap: 9px; }
  .contacts svg { width: 12px; height: 12px; flex: none; }
</style>
</head>
<body>

<section class="card card--front" aria-label="Card front">
  <div class="brand"><span class="brand__dot"></span>Greenloop Recovery</div>
</section>

<section class="card card--back" aria-label="Card back">
  <svg class="card__shapes" viewBox="0 0 540 309" preserveAspectRatio="none" aria-hidden="true">
    <defs>
      <linearGradient id="bandGrad" x1="0" y1="0" x2="1" y2="0">
        <stop offset="0" stop-color="#5fb14a"/>
        <stop offset="1" stop-color="#a6d13c"/>
      </linearGradient>
      <linearGradient id="wedgeGrad" x1="0" y1="1" x2="1" y2="0">
        <stop offset="0" stop-color="#1f6637"/>
        <stop offset="1" stop-color="#2a8c4d"/>
      </linearGradient>
    </defs>
    <polygon points="0,0 232,0 206,96 0,96" fill="url(#wedgeGrad)"/>
    <polygon points="232,0 252,0 226,96 206,96" fill="#a6d13c"/>
    <polygon points="252,0 540,0 540,13 249,13" fill="url(#bandGrad)"/>
  </svg>

  <div class="holder">
    <p class="holder__name">Daniel Hart</p>
    <p class="holder__role">Manager</p>
  </div>

  <div class="brand"><span class="brand__dot"></span>Greenloop Recovery</div>

  <p class="address">Your address, city<br>state, ZIP 0000</p>

  <ul class="contacts">
    <li>
      <svg viewBox="0 0 12 12" aria-hidden="true"><path d="M2 1.5l2 0 1 2.5-1.2 1a6 6 0 0 0 3.2 3.2l1-1.2 2.5 1v2a1 1 0 0 1-1 1A9 9 0 0 1 1 2.5a1 1 0 0 1 1-1z" fill="#6cb543"/></svg>
      555-014-7382
    </li>
    <li>
      <svg viewBox="0 0 12 12" aria-hidden="true"><rect x="1" y="2.5" width="10" height="7" fill="none" stroke="#6cb543" stroke-width="1.1"/><path d="M1 2.5l5 4 5-4" fill="none" stroke="#6cb543" stroke-width="1.1"/></svg>
      hello@greenloop.example
    </li>
    <li>
      <svg viewBox="0 0 12 12" aria-hidden="true"><circle cx="6" cy="6" r="5" fill="none" stroke="#6cb543" stroke-width="1.1"/><ellipse cx="6" cy="6" rx="2.2" ry="5" fill="none" stroke="#6cb543" stroke-width="1"/><path d="M1 6h10" stroke="#6cb543" stroke-width="1"/></svg>
      www.greenloop.example
    </li>
  </ul>
</section>

</body>
</html>
```